Pro-Athlete Founded Charity Seeks Letterhead Design

A non-profit organization, called Passes for "Discovery: The Dale Wiston Trust," was founded by an PGL athelete to help children born with cardiac heart defects. The charity funds this initiative under the name, "The KINDest Field."

Please create a letterhead considering the following requirements:

- Use Dominant logo: The Kindest Field

- Use Auxillary logo: Passes for Discovery

- Address:4620 North Willow Parkway Second Floor, Boca Raton, FL 33418

- Website: www.passesfordiscovery-example.org

- Editable places for date; letter recipients' name/address; signature block

- Coloring: Coastal Herons blue/black (athlete plays for that PGL team); and red (for cardiology/heart disease)... reference logos

Thanks to any and all designers who work on this project! A winner WILL be selected, and follow-on projects will be requested of the winning designer.

```html
<!DOCTYPE html>
<html lang="en">
<head>
<meta charset="utf-8">
<title>Passes for Discovery Letterhead</title>
<link href="https://fonts.googleapis.com/css2?family=Lato:wght@400;700&display=swap" rel="stylesheet">
<style>
  :root {
    --ink: #161616;
    --body: #3b3b3b;
    --heart-red: #d62027;
    --heron-blue: #1fa9d6;
    --paper: #ffffff;
  }
  * { margin: 0; padding: 0; box-sizing: border-box; }
  html, body { width: 927px; height: 1200px; overflow: hidden; background: var(--paper); }
  .letterhead {
    position: relative; width: 927px; height: 1200px;
    font-family: "Lato", Arial, sans-serif; color: var(--body);
  }
  .rule-pair { position: absolute; }
  .rule-pair span { display: block; height: 3px; background: var(--ink); }
  .rule-pair span + span { margin-top: 6px; }
  .rule-top-left { left: 27px; top: 75px; width: 212px; }
  .rule-top-right { left: 707px; top: 75px; width: 193px; }
  .primary-mark {
    position: absolute; left: 248px; top: 38px; width: 126px;
    display: flex; flex-direction: column; align-items: center; gap: 10px;
  }
  .primary-mark .dot { width: 56px; height: 56px; border-radius: 50%; background: var(--heart-red); }
  .primary-mark .name {
    font-weight: 700; font-size: 14px; color: var(--ink); text-align: center; white-space: nowrap;
  }
  .org-block { position: absolute; left: 400px; top: 33px; color: var(--ink); }
  .org-name { font-weight: 700; font-size: 21.5px; line-height: 29px; }
  .org-address { font-weight: 700; font-size: 15.5px; line-height: 20px; margin-top: 1px; }
  .letter {
    position: absolute; left: 35px; top: 198px; width: 848px;
    font-size: 15.7px; line-height: 23.4px;
  }
  .letter .date { margin-bottom: 54px; }
  .letter .recipient { line-height: 19.8px; margin-bottom: 53px; }
  .letter p { margin-bottom: 15px; }
  .letter .salutation { margin-bottom: 13px; }
  .letter .signature { line-height: 19.8px; padding-top: 45px; }
  .rule-bottom { position: absolute; top: 1114px; height: 3px; background: var(--ink); }
  .rule-bottom-left { left: 27px; width: 370px; }
  .rule-bottom-right { left: 535px; width: 365px; }
  .secondary-mark {
    position: absolute; left: 405px; top: 1100px; width: 122px;
    display: flex; flex-direction: column; align-items: center; gap: 5px;
  }
  .secondary-mark .dot { width: 14px; height: 14px; border-radius: 50%; background: var(--heron-blue); }
  .secondary-mark .name { font-weight: 700; font-size: 12.5px; color: var(--ink); white-space: nowrap; }
  .website {
    position: absolute; left: 0; width: 927px; top: 1157px; text-align: center;
    font-weight: 700; font-size: 16px; color: var(--ink);
  }
</style>
</head>
<body>
<div class="letterhead">
  <div class="rule-pair rule-top-left"><span></span><span></span></div>
  <div class="rule-pair rule-top-right"><span></span><span></span></div>

  <div class="primary-mark">
    <div class="dot"></div>
    <div class="name">The Kindest Field</div>
  </div>

  <div class="org-block">
    <div class="org-name">Passes for Discovery:<br>The Dale Wiston Trust</div>
    <div class="org-address">4620 North Willow Parkway<br>Second Floor | Boca Raton, FL 33418</div>
  </div>

  <div class="letter">
    <div class="date">[Insert Date]</div>
    <div class="recipient">[Recipient]<br>[Title]<br>[Company]<br>[Address 1]<br>[Address 2]<br>[Address 3]</div>
    <p class="salutation">Dear [Recipient]:</p>
    <p>Fusce neque mi, consectetuer gravida, convallis ac, varius a, pede. Fusce pellentesque pretium quam. Ut luctus, justo id volutpat iaculis, est diam pulvinar sem, quis bibendum turpis dui eget mauris. Sed in mauris. Ut massa. Pellentesque condimentum felis nec sapien. Integer posuere elit at turpis. Nulla facilisi. Sed sapien ipsum, commodo ut, facilisis vitae, ultrices non, metus. Aenean non nulla. Curabitur molestie volutpat magna. Vestibulum tempor faucibus nisi. Pellentesque vitae enim.</p>
    <p>Aliquam rhoncus volutpat mauris. Sed auctor. Donec tincidunt velit et tellus. Donec sed augue eget lacus placerat adipiscing. Ut convallis suscipit nulla. Morbi posuere ullamcorper ligula. Duis sit amet odio nec lorem ornare gravida. Suspendisse ante nulla, gravida quis, eleifend sit amet, placerat eget, purus. Sed egestas magna ut erat. Vivamus euismod, odio id mattis porttitor, tellus nisl consectetuer turpis, ut auctor enim justo euismod nulla. Fusce eget diam vulputate massa tempor tempor.</p>
    <p>In ante. Phasellus convallis, nisl in vestibulum facilisis, lacus pede bibendum urna, dapibus pellentesque eros magna sed nibh. Etiam tortor arcu, porta nec, laoreet quis, mollis in, libero. Aenean dapibus est a metus. In sit amet elit. Pellentesque luctus lacus scelerisque arcu. Cras mattis diam. Sed molestie, lectus id bibendum luctus, magna orci luctus quam, et auctor urna diam sit amet ligula. Sed purus dui, suscipit et, malesuada non, consectetuer in, augue. Proin et sapien. Maecenas aliquam, nibh id aliquet tincidunt, ante neque pulvinar mauris, sit amet fermentum nibh augue mollis risus. Mauris porttitor varius mauris. Vivamus in urna et sem accumsan imperdiet. Aenean fringilla, eros tincidunt gravida elementum, justo eros pharetra felis, in rhoncus arcu lectus non enim. Phasellus odio tortor, mattis ut, mattis elementum, luctus at, orci.</p>
    <p>Sincerely,</p>
    <div class="signature">Name<br>[Your Title]</div>
  </div>

  <div class="rule-bottom rule-bottom-left"></div>
  <div class="rule-bottom rule-bottom-right"></div>
  <div class="secondary-mark">
    <div class="dot"></div>
    <div class="name">Passes for Discovery</div>
  </div>
  <div class="website">www.passesfordiscovery-example.org</div>
</div>
</body>
</html>
```